Gin Bottle label

Hi, I would like a design based on a traditional, Vintage, Victorian type label.
The product is 'Hawthorn & Sloeberry Gin'
It will be 50cl and 40% vol.
The Gin will be dark brown in colour and attached is the types of bottle and a few ideas of the styles I like.
Many Thanks

```html
<!DOCTYPE html>
<html lang="en">
<head>
<meta charset="utf-8">
<title>Hawthorn &amp; Sloeberry Gin – Label</title>
<link rel="stylesheet" href="https://fonts.googleapis.com/css2?family=Sancreek&family=Berkshire+Swash&family=Playfair+Display:wght@400;700&family=Oswald:wght@500&display=swap">
<style>
  :root {
    --paper: #f2ead2;
    --paper-shade: #e6dcbf;
    --ink: #161412;
    --ink-soft: #3b3835;
    --ornament: #c9bfa3;
  }
  * { box-sizing: border-box; margin: 0; padding: 0; }
  html, body { width: 972px; height: 1200px; overflow: hidden; background: var(--paper); }
  .label {
    position: relative;
    width: 972px;
    height: 1200px;
    background: radial-gradient(ellipse at 50% 45%, var(--paper) 55%, var(--paper-shade) 100%);
    color: var(--ink);
    overflow: hidden;
  }
  .frame { position: absolute; inset: 0; }
  .ornament {
    position: absolute;
    background: var(--ornament);
    opacity: .75;
    z-index: 0;
  }
  .corner-tl { left: 64px;  top: 29px;   width: 134px; height: 134px; border-radius: 0 0 70% 0; }
  .corner-tr { right: 64px; top: 29px;   width: 134px; height: 134px; border-radius: 0 0 0 70%; }
  .corner-bl { left: 64px;  bottom: 36px; width: 134px; height: 150px; border-radius: 0 70% 0 0; }
  .corner-br { right: 64px; bottom: 36px; width: 134px; height: 150px; border-radius: 70% 0 0 0; }
  .swirl-left  { left: 90px;  top: 700px; width: 130px; height: 130px; border-radius: 50%; }
  .swirl-right { right: 90px; top: 700px; width: 130px; height: 130px; border-radius: 50%; }
  .flourish-title-top { left: 240px; top: 160px; width: 80px; height: 40px; border-radius: 50%; }
  .flourish-title-mid { left: 620px; top: 385px; width: 90px; height: 50px; border-radius: 50%; }
  .flourish-title-low { left: 640px; top: 642px; width: 90px; height: 40px; border-radius: 50%; }
  .flourish-gin { left: 273px; top: 972px; width: 424px; height: 60px; border-radius: 50%; }

  .quality-banner {
    position: absolute;
    left: 337px; top: 74px;
    width: 307px; height: 58px;
    border: 2px solid var(--ink-soft);
    border-radius: 6px;
    display: flex; align-items: center; justify-content: center;
    font-family: "Oswald", sans-serif;
    font-weight: 500;
    font-size: 21px;
    letter-spacing: 2px;
    color: var(--ink-soft);
  }
  .title { position: relative; z-index: 1; }
  .product-name {
    position: absolute;
    left: 0; right: 0;
    text-align: center;
    font-family: "Sancreek", serif;
    font-weight: 400;
    line-height: 1;
    color: var(--ink);
  }
  .name-first  { top: 215px; font-size: 150px; letter-spacing: -2px; }
  .name-amp    { top: 425px; font-size: 80px; font-family: "Berkshire Swash", serif; }
  .name-second { top: 495px; font-size: 128px; letter-spacing: -2px; }
  .spirit {
    position: absolute;
    left: 0; right: 0; top: 712px;
    text-align: center;
    font-family: "Berkshire Swash", serif;
    font-weight: 400;
    font-size: 200px;
    line-height: 1;
  }
  .measure {
    position: absolute;
    top: 1066px;
    font-family: "Playfair Display", serif;
    font-variant-numeric: lining-nums;
    font-size: 54px;
    line-height: 1;
    z-index: 1;
  }
  .volume  { left: 258px; }
  .strength { left: 530px; }
  .dot-rule { position: absolute; left: 250px; top: 1138px; }
</style>
</head>
<body>
<main class="label">
  <svg class="frame" width="972" height="1200" viewBox="0 0 972 1200" aria-hidden="true">
    <rect x="10" y="8" width="952" height="1184" fill="none" stroke="#3b3835" stroke-width="4"/>
    <rect x="24" y="22" width="924" height="1156" fill="none" stroke="#3b3835" stroke-width="2"/>
  </svg>

  <div class="ornament corner-tl" role="img" aria-label="Victorian filigree corner ornament"></div>
  <div class="ornament corner-tr" role="img" aria-label="Victorian filigree corner ornament"></div>
  <div class="ornament corner-bl" role="img" aria-label="Victorian filigree corner ornament"></div>
  <div class="ornament corner-br" role="img" aria-label="Victorian filigree corner ornament"></div>
  <div class="ornament swirl-left" role="img" aria-label="Scroll swirl ornament"></div>
  <div class="ornament swirl-right" role="img" aria-label="Scroll swirl ornament"></div>
  <div class="ornament flourish-title-top" role="img" aria-label="Small scroll flourish"></div>
  <div class="ornament flourish-title-mid" role="img" aria-label="Small scroll flourish"></div>
  <div class="ornament flourish-title-low" role="img" aria-label="Small scroll flourish"></div>
  <div class="ornament flourish-gin" role="img" aria-label="Ornate scroll divider"></div>

  <div class="quality-banner">HIGHEST QUALITY</div>

  <h1 class="title">
    <span class="product-name name-first">Hawthorn</span>
    <span class="product-name name-amp">&amp;</span>
    <span class="product-name name-second">Sloeberry</span>
    <span class="spirit">Gin</span>
  </h1>

  <p class="measure volume">50 cl</p>
  <p class="measure strength">40%vol.</p>

  <svg class="dot-rule" width="482" height="12" viewBox="0 0 482 12" aria-hidden="true">
    <g fill="#3b3835">
      <circle cx="4" cy="6" r="2"/><circle cx="24" cy="6" r="2.5"/><circle cx="46" cy="6" r="3"/>
      <circle cx="70" cy="6" r="3"/><circle cx="95" cy="6" r="3.5"/><circle cx="121" cy="6" r="3.5"/>
      <circle cx="148" cy="6" r="4"/><circle cx="176" cy="6" r="4"/><circle cx="205" cy="6" r="4.5"/>
      <circle cx="241" cy="6" r="5"/><circle cx="277" cy="6" r="4.5"/><circle cx="306" cy="6" r="4"/>
      <circle cx="334" cy="6" r="4"/><circle cx="361" cy="6" r="3.5"/><circle cx="387" cy="6" r="3.5"/>
      <circle cx="412" cy="6" r="3"/><circle cx="436" cy="6" r="3"/><circle cx="458" cy="6" r="2.5"/>
      <circle cx="478" cy="6" r="2"/>
    </g>
  </svg>
</main>
</body>
</html>
```